Jahresprogramm für kirchliche Organisation
Zielgruppe
Wir sind die Berufungspastoralstelle im Bistum Halbrode der katholischen Kirche. Wir kümmen uns um die Frage nach der Berufung von jungen Menschen zwischen 17-30 Jahren. Unter Berufung verstehen wir die Frage nach dem Plan Gottes für das eigene Leben
Aufgabenstellung
Es geht um eine Designvorlage für eine Jahresprospekt unserer Stelle, die wir leicht wieder ändern oder ergänzen können (Grafikprogrammgrundkenntnisse sind vorhanden), da manche Termine noch nicht letzlich feststehen.
Vom Design darf es sich gerne an unserer Homepage https://www.lebenswegstelle-halbrode.de/ orientieren.
Wenn möglich gerne im Endformat DIN lang quer (210 x 105 mm)

```html
<!DOCTYPE html>
<html lang="de">
<head>
<meta charset="utf-8">
<title>Jahresprogramm 2022 – Weg &amp; Ziel</title>
<link rel="stylesheet" href="https://fonts.googleapis.com/css2?family=Open+Sans:wdth,wght@75,300;75,400;75,700&display=swap">
<style>
  :root {
    --page-bg: #ffffff;
    --card-bg: #ffffff;
    --accent-gold: #e4b424;
    --ink: #111111;
    --ink-soft: #555555;
    --band-black: #000000;
    --photo-light: #e9dccd;
    --photo-mid: #b8a28a;
    --photo-dark: #8d7560;
  }
  * { margin: 0; padding: 0; box-sizing: border-box; }
  html, body {
    width: 1200px; height: 675px; overflow: hidden;
    background: var(--page-bg);
  }
  body {
    position: relative;
    font-family: "Open Sans", Arial, sans-serif;
    font-stretch: 75%;
  }
  .flyer-cover {
    position: absolute;
    left: 153px; top: 114px;
    width: 893px; height: 447px;
    background: var(--card-bg);
    box-shadow: 0 2px 10px rgba(0,0,0,0.25);
    overflow: hidden;
  }
  .accent-stripe {
    position: absolute; left: 0; top: 0;
    width: 42px; height: 100%;
    background: var(--accent-gold);
  }
  .cover-photo {
    position: absolute; left: 42px; top: 0;
    width: 456px; height: 100%;
    background:
      radial-gradient(ellipse 120px 260px at 42% 40%, rgba(245,240,232,0.95), rgba(245,240,232,0) 100%),
      radial-gradient(ellipse at 85% 10%, #f3e4e2 0%, rgba(243,228,226,0) 55%),
      linear-gradient(180deg, var(--photo-mid) 0%, var(--photo-light) 35%, var(--photo-mid) 70%, var(--photo-dark) 100%);
  }
  .info-panel {
    position: absolute; left: 498px; top: 0;
    width: 395px; height: 100%;
  }
  .brand-name {
    position: absolute; right: 56px; top: 68px;
    font-size: 30px; font-weight: 400; line-height: 1;
    color: var(--ink); white-space: nowrap;
  }
  .diocese {
    position: absolute; right: 56px; top: 156px;
    display: flex; align-items: center; gap: 8px;
  }
  .diocese .square {
    width: 12px; height: 12px; background: var(--ink);
  }
  .diocese .name {
    font-size: 17px; font-weight: 300; letter-spacing: 1.5px;
    color: var(--ink); text-transform: uppercase; line-height: 1;
  }
  .year {
    position: absolute; right: 53px; top: 258px;
    font-size: 68px; font-weight: 700; line-height: 1;
    color: var(--ink);
  }
  .motto {
    position: absolute; right: 53px; top: 342px;
    font-size: 27px; font-weight: 300; line-height: 1;
    color: var(--ink-soft); white-space: nowrap;
  }
  .footer-band {
    position: absolute; left: 0; bottom: 0;
    width: 100%; height: 33px;
    background: var(--band-black);
  }
</style>
</head>
<body>
  <section class="flyer-cover">
    <div class="accent-stripe"></div>
    <div class="cover-photo" role="img" aria-label="Foto: barfüßige Person in weißem Gewand geht einen sandigen Weg entlang, warmes Gegenlicht"></div>
    <div class="info-panel">
      <p class="brand-name">Weg &amp; Ziel</p>
      <div class="diocese">
        <span class="square"></span>
        <span class="name">Bistum Halbrode</span>
      </div>
      <h1 class="year">2022</h1>
      <p class="motto">Komm und sieh!&nbsp; Joh 1,46</p>
      <div class="footer-band"></div>
    </div>
  </section>
</body>
</html>
```